Promotional Flyer/Email Design - Cabling services for Broadcast and Audio Visual

We need a promotional flyer/email design to help launch our company, Velcor Lane. We provide cabling services for Broadcast Television and Audio Visual systems. Recent projects include major television events such as the Harrowmere Racquet Classic and Audio Visual/Entertainment systems for wealthy clients in their homes and on-board super yachts.

The flyer will be printed as single sided A5 and also be sent out in the body of a promotional email. It should feature the company logo along with a complementary colour scheme. It should have a clean finish with images that show the type of work we do (cabling and equipment installation) or the setting for these systems (tv studio, super yacht, cinema room, meeting room with projector etc.)

Services we offer are:

Broadcast/AV system design
On-site installation
Rack building
Pre-fabricated cable looms
Fibre optic installation

About the company:

Velcor Lane provide cabling services for Broadcast Television and Audio Visual systems. With over 15 years experience working in these industries we can help with every aspect of design, project managment, installation and maintenance. Our projects range from fibre optic cabling at major sports events to installing and commisioning bespoke control systems on some of the worlds largest super yachts.

Contact details:

To get a quote or discuss your project contact us now
Telephone: TBC
Email: info@velcor-lane.com
Website: www.velcor-lane.com
Address: TBC

Other information:

The company is based in London, UK. Our projects often take place in other countries with work taking place accross Europe and beyond.

We have a London based workshop for rack building and cable pre-fabrication.

Our website is www.velcor-lane.com

Images:

Images attached can be editted for use on the flyer or have ideas taken from them. Only the company logo is required to feature on the final design.

Target Market(s)

Business to business

Industry/Entity Type

It Company

Font styles to use
Sans Serif

Requirements
Must have
• Company logo
• List of services
• Contact details
Nice to have
• Image of cabling, home cinema room, super yacht, luxury home, outside broadcast truck, fibre optic equipment or cabling.

```html
<!DOCTYPE html>
<html lang="en">
<head>
<meta charset="utf-8">
<title>Velcor Lane – Here We Go!</title>
<link rel="stylesheet" href="https://fonts.googleapis.com/css2?family=Montserrat:ital,wght@0,300;0,400;0,500;0,600;0,800;1,700&display=swap">
<style>
  :root {
    --page-bg: #c9d3da;
    --paper: #f4f5f6;
    --ink: #4a4c4f;
    --ink-soft: #5d6063;
    --accent: #4f9fb8;
    --corner-blue: #5672c4;
    --photo-dark: #1f3a3c;
    --photo-mid: #3d6a6a;
    --photo-light: #7fa5a3;
    --white: #ffffff;
  }
  * { margin: 0; padding: 0; box-sizing: border-box; }
  html, body { width: 1200px; height: 700px; overflow: hidden; }
  body {
    background: var(--page-bg);
    font-family: "Montserrat", sans-serif;
    color: var(--ink);
    position: relative;
  }
  .flyer {
    position: absolute;
    left: 360px; top: 10px;
    width: 480px; height: 680px;
    background: var(--paper);
    overflow: hidden;
    box-shadow: 0 8px 24px rgba(40, 55, 65, 0.25);
  }
  .hero-photo {
    position: absolute; left: 0; top: 0;
    width: 100%; height: 380px;
    background:
      linear-gradient(90deg, rgba(20,40,42,0.55) 0%, rgba(20,40,42,0) 30%, rgba(20,40,42,0) 70%, rgba(20,40,42,0.7) 100%),
      linear-gradient(180deg, var(--photo-dark) 0%, var(--photo-mid) 55%, var(--photo-light) 100%);
  }
  .brand {
    position: absolute; left: 0; top: 200px; width: 100%;
    text-align: center; color: var(--white);
  }
  .brand-name {
    display: inline-flex; align-items: center; gap: 14px;
    font-size: 34px; font-weight: 400; letter-spacing: 10px;
  }
  .brand-mark {
    width: 14px; height: 14px; background: var(--white);
  }
  .brand-tagline {
    margin-top: 8px;
    font-size: 9px; font-weight: 500; letter-spacing: 3.2px;
  }
  .headline {
    position: absolute; left: 0; top: 392px; width: 100%;
    text-align: center;
    font-size: 58px; font-weight: 800; letter-spacing: 1px;
    color: var(--ink);
  }
  .rule {
    position: absolute; left: 36px; right: 36px; top: 470px;
    height: 1px; background: var(--ink);
  }
  .section-title {
    font-size: 15px; font-weight: 300; letter-spacing: 1px;
    color: var(--ink);
    margin-bottom: 6px;
  }
  .section-title strong { font-weight: 700; color: var(--accent); }
  .about {
    position: absolute; left: 36px; top: 482px; width: 196px;
  }
  .about p {
    font-size: 7.4px; line-height: 1.45; font-weight: 500; color: var(--ink-soft);
  }
  .services {
    position: absolute; left: 256px; top: 482px; width: 200px;
  }
  .services ul { list-style: none; }
  .services li {
    font-size: 10.5px; font-weight: 500; line-height: 1.4; color: var(--ink-soft);
  }
  .services li::before { content: "•"; margin-right: 4px; }
  .cta {
    position: absolute; left: 36px; right: 36px; top: 600px;
    text-align: center;
    font-size: 8.5px; font-weight: 700; font-style: italic; color: var(--ink-soft);
  }
  .contact {
    position: absolute; left: 60px; top: 620px; width: 260px;
    display: grid; grid-template-columns: 1fr 1fr; row-gap: 10px;
    font-size: 8px; font-weight: 500; color: var(--ink-soft);
  }
  .contact-item { display: flex; align-items: center; gap: 8px; }
  .contact-item svg { width: 12px; height: 12px; fill: var(--ink); flex: none; }
  .footer-brand {
    position: absolute; right: 56px; top: 640px;
    display: flex; align-items: center; gap: 6px;
    font-size: 15px; font-weight: 600; color: var(--ink);
  }
  .footer-brand .brand-mark { width: 10px; height: 10px; background: var(--corner-blue); }
  .corner { position: absolute; background: var(--corner-blue); }
  .corner-left { left: 0; top: 590px; width: 22px; height: 90px; }
  .corner-right { right: 0; bottom: 0; width: 30px; height: 22px; opacity: 0.8; }
</style>
</head>
<body>
  <article class="flyer">
    <div class="hero-photo" role="img" aria-label="Photo of equipment racks with dense cabling, tinted teal"></div>

    <div class="brand">
      <div class="brand-name"><span>VELCOR</span><span class="brand-mark"></span><span>LANE</span></div>
      <div class="brand-tagline">BROADCAST TELEVISION AND AUDIO VISUAL SYSTEMS</div>
    </div>

    <h1 class="headline">HERE WE GO !</h1>
    <div class="rule"></div>

    <section class="about">
      <h2 class="section-title">ABOUT <strong>US</strong></h2>
      <p>Velcor Lane provide cabling services for Broadcast Television and Audio Visual systems. With over 15 years experience working in these industries we can help with every aspect of design, project management, installation and maintenance. Our projects range from fibre optic cabling at major sports events to installing and commissioning bespoke control systems on some of the worlds largest super yachts.</p>
    </section>

    <section class="services">
      <h2 class="section-title">OUR <strong>SERVICES</strong></h2>
      <ul>
        <li>Broadcast/AV system design</li>
        <li>On-site installation</li>
        <li>Rack building</li>
        <li>Pre-fabricated cable looms</li>
        <li>Fibre optic installation</li>
      </ul>
    </section>

    <p class="cta">To get a quote or discuss your project contact us now</p>

    <div class="contact">
      <div class="contact-item">
        <svg viewBox="0 0 12 12"><path d="M6 0a4 4 0 0 0-4 4c0 3 4 8 4 8s4-5 4-8a4 4 0 0 0-4-4zm0 5.5A1.5 1.5 0 1 1 6 2.5a1.5 1.5 0 0 1 0 3z"/></svg>
        <span>London, UK</span>
      </div>
      <div class="contact-item">
        <svg viewBox="0 0 12 12"><path d="M3.2 0.5 1 1.2C0.6 4.8 6 11.4 10.8 11l.7-2.2-2.6-1.4-1.2 1.2C6 8 4 6 3.4 4.3l1.2-1.2z"/></svg>
        <span>(010) 555 0142</span>
      </div>
      <div class="contact-item">
        <svg viewBox="0 0 12 12"><path d="M0 2h12v8H0z M0 2l6 4.5L12 2" stroke="#f4f5f6" stroke-width="0.8"/></svg>
        <span>info@velcor-lane.com</span>
      </div>
      <div class="contact-item">
        <svg viewBox="0 0 12 12"><circle cx="6" cy="6" r="5.5"/><path d="M0.5 6h11M6 0.5v11M6 0.5c-3 3-3 8 0 11M6 0.5c3 3 3 8 0 11" stroke="#f4f5f6" stroke-width="0.7" fill="none"/></svg>
        <span>www.velcor-lane.com</span>
      </div>
    </div>

    <div class="footer-brand"><span class="brand-mark"></span><span>Velcor Lane</span></div>

    <div class="corner corner-left"></div>
    <div class="corner corner-right"></div>
  </article>
</body>
</html>
```